Label

I need a label designed for a bottle of water. I like the lightning bolt and the blue. But I do not want it exactly like the Zimm-ooh.

The label needs to be 9 inches by 2.5 inches.

Logo Text

Mesa Spring: Sip the Mesa

```html
<!DOCTYPE html>
<html lang="en">
<head>
<meta charset="utf-8">
<title>Mesa Spring – Bottle Label</title>
<link href="https://fonts.googleapis.com/css2?family=Roboto+Condensed:wght@700&display=swap" rel="stylesheet">
<style>
  :root {
    --canvas: #ffffff;
    --label-blue: #2b7fd8;
    --label-blue-deep: #3a63c9;
    --brand-white: #ffffff;
  }
  html, body {
    margin: 0;
    padding: 0;
    width: 1197px;
    height: 1200px;
    overflow: hidden;
    background: var(--canvas);
  }
  .canvas {
    position: relative;
    width: 1197px;
    height: 1200px;
  }
  .label {
    position: absolute;
    left: 114px;
    top: 472px;
    width: 980px;
    height: 273px;
    background: linear-gradient(90deg, var(--label-blue), var(--label-blue-deep) 50%, var(--label-blue));
    display: flex;
    align-items: center;
    justify-content: center;
  }
  .brand-name {
    margin: 0;
    font-family: "Roboto Condensed", "Arial Narrow", sans-serif;
    font-weight: 700;
    font-size: 80px;
    line-height: 68px;
    color: var(--brand-white);
    text-align: center;
    letter-spacing: 0;
    transform: translate(-44px, 4px);
  }
  .brand-name span {
    display: block;
  }
</style>
</head>
<body>
  <main class="canvas">
    <section class="label" role="img" aria-label="Blue bottle label band">
      <h1 class="brand-name">
        <span class="brand-line">Mesa Spring</span>
        <span class="brand-line">Sip the Mesa</span>
      </h1>
    </section>
  </main>
</body>
</html>
```